Mens Jewellery Homepage - Modern, Stylish Mens Ring Brand - Homepage

Project Overview: TorvikLoops.com is a men's accessories brand specializing in high-quality mens rings.

The objective of this redesign is to create a modern, visually appealing homepage that is easy to navigate, showcases a wide range of rings, highlights personalization options, and builds trust with customers.

The new design should make a strong impression while reflecting the brand's premium quality and commitment to craftsmanship.

The focus will be on a sleek aesthetic that aligns with the tastes of men shopping for wedding bands, engagement rings, or fashion accessories.

Objectives:

Modern and Sleek Aesthetic:

A clean, minimalist design that emphasizes high-quality product imagery and thoughtful use of space.
Contemporary color palette that conveys elegance and sophistication, with accents that highlight key elements without overwhelming the user.

Consistent and easy-to-read typography that reflects the brand’s modern and masculine identity.

Showcasing Products:
Hero Section: A image to show off 3 or 4 ring designs that could be used for weddings or fashion.

Product Highlights: Below the hero banner, showcase product categories by color (see current website for colors)

Featured Products: Display a selection of “Top Rated” or “Customer Favorites” rings to help guide users toward popular choices.

Personalization Section:
A dedicated section promoting the ability to personalize rings, emphasizing features like engraving with names, dates, or special messages.
Include lifestyle images of personalized rings to inspire customers and give them an idea of what’s possible.
Use callouts such as “Make It Yours” or “Personalize Your Ring” to encourage users to explore the customization options available for each product.

Building Trust:

A space to show 5 or 6 testimonials and other trust elements

Symbols / text to show

free delivery
free returns
every ring stock
fast delivery
customer images (from reviews)

Driving Conversions:
Include a prominent call-to-action (CTA) button in the hero section with text like “Shop Now” or “Discover Our Collections.”

User Experience:
Fast, easy-to-navigate layout with simple and intuitive categories. Product categories and main sections should be clearly visible and easy to access without overwhelming the user.
Design the homepage to feel cohesive and uncluttered, with a logical flow from product discovery to personalization and checkout.

Visual Elements and Imagery:
Use ring images from our site, but add backgrounds etc to make the image on the homepage more interesting.

Personalization Options: Use visual representations (like ring mockups) showing where personalization options (such as engravings) would appear on the product.

I like (and would like to see some different designs from our current design)
Brix.com for design
stoutcircles.com

Target Market(s)

Men - 20 to 35

Number of Pages Required

1 page

Requirements
Must have
• Easy navigation, Trust, Modern, Clean,
Nice to have
• Would like to see Different designs like Brix.com - StoutCircles.com

```html
<!DOCTYPE html>
<html lang="en">
<head>
<meta charset="utf-8">
<title>Torvik Loops – Men's Rings</title>
<link href="https://fonts.googleapis.com/css2?family=Outfit:wght@300;400;500;600;700&display=swap" rel="stylesheet">
<style>
:root{
  --ink:#111;
  --gold:#d79a2b;
  --cream:#fdf3ea;
  --white:#fff;
}
*{box-sizing:border-box;margin:0;padding:0}
html,body{width:1200px;height:5268px;overflow:hidden}
body{font-family:'Outfit',sans-serif;color:var(--ink);background:var(--white);position:relative}
.abs{position:absolute}
/* header */
.header{top:0;left:0;width:1200px;height:118px;background:var(--white)}
.brand{left:70px;top:18px;display:flex;align-items:center;gap:12px}
.brand-dot{width:84px;height:84px;border:5px solid var(--ink);border-radius:50%;flex:none}
.brand-name{font-size:28px;font-weight:500;letter-spacing:9px;line-height:1.2;white-space:nowrap}
.nav{right:62px;top:66px;display:flex;gap:26px;font-size:13px;text-transform:uppercase;white-space:nowrap}
.nav a{color:var(--ink);text-decoration:none;padding-bottom:8px}
.nav a.active{color:var(--gold);border-bottom:2px solid var(--gold)}
.search{left:888px;top:24px;width:192px;height:30px;border:1.5px solid #999;border-radius:15px;font-size:11px;color:#888;padding:7px 14px}
.cart{left:1098px;top:26px}
/* hero */
.hero{top:118px;left:0;width:1200px;height:672px;background:linear-gradient(90deg,#b8a89b 0%,#d8cdc3 35%,#ece6df 70%,#f2eeea 100%)}
.hero-circle{left:560px;top:168px;width:556px;height:556px;border-radius:50%;background:var(--white);text-align:center;padding-top:66px}
.eyebrow{font-size:21px;font-weight:500}
.hero-title{font-size:45px;font-weight:400;line-height:1.32;margin-top:16px}
.btn{display:inline-flex;align-items:center;gap:24px;background:var(--ink);color:var(--white);font-weight:600;font-size:16px;text-transform:uppercase;border-radius:6px;text-decoration:none;white-space:nowrap}
.btn .arr{width:24px;height:24px;border-radius:50%;background:var(--gold);display:inline-flex;align-items:center;justify-content:center;flex:none}
.hero-circle .btn{margin-top:26px;padding:20px 30px 20px 36px;font-size:17px}
/* features */
.features{top:790px;left:0;width:1200px;height:325px;background:var(--cream)}
.feature{top:62px;width:240px;text-align:center;font-weight:600;font-size:19px;text-transform:uppercase}
.feature .ring{width:144px;height:144px;margin:0 auto 28px;border:2px dotted var(--ink);border-radius:50%;display:flex;align-items:center;justify-content:center}
.feature .core{width:124px;height:124px;border-radius:50%;background:var(--ink);display:flex;align-items:center;justify-content:center}
/* section heads */
.sec-head{left:0;width:1200px;text-align:center}
.emblem{display:flex;align-items:center;justify-content:center;gap:12px}
.emblem i{display:block;width:56px;height:2px;background:var(--gold)}
.emblem b{width:40px;height:40px;border:3px solid var(--ink);border-radius:50%}
.sec-title{font-size:56px;font-weight:400;margin-top:6px}
/* filter */
.filter-title{left:66px;top:1340px;font-size:22px;font-weight:500}
.filter-label{top:1380px;font-size:19px;white-space:nowrap}
.select{top:1373px;width:180px;height:38px;background:var(--white);box-shadow:0 1px 6px rgba(0,0,0,.18)}
.select:after{content:"";position:absolute;right:14px;top:15px;border:6px solid transparent;border-top:8px solid var(--ink)}
.filter-line{left:66px;top:1440px;width:1068px;height:2px;background:var(--gold)}
/* categories */
.cat{width:342px}
.cat .tile{height:410px;text-align:center;color:var(--white);padding-top:38px}
.cat .the{font-size:22px;font-weight:300}
.cat .name{font-size:58px;font-weight:600;line-height:1.05;white-space:nowrap}
.cat .coll{font-size:21px;font-weight:300}
.cat .label{display:flex;align-items:center;gap:24px;font-size:22px;font-weight:600;margin-top:14px;white-space:nowrap}
.cat .label i{width:54px;height:2px;background:var(--gold);position:relative}
.cat .label i:after{content:"";position:absolute;right:0;top:-4px;border:5px solid transparent;border-left:7px solid var(--gold)}
/* products */
.card{width:342px;height:482px;background:var(--white);box-shadow:0 2px 10px rgba(0,0,0,.16);padding:8px}
.card .img{height:282px}
.card h3{font-size:21px;font-weight:500;line-height:1.2;margin:28px 14px 0}
.card .price{margin:22px 14px 0;font-size:19px;font-weight:500}
.card .price s{color:#aaa;margin-right:18px}
.card .mini{margin:14px 14px 0;padding:9px 16px;font-size:11px;border-radius:5px}
.cta{left:453px;width:292px;height:64px;justify-content:center}
/* personalization */
.personal{top:3450px;left:0;width:1200px;height:550px;background:linear-gradient(90deg,#2f2f2f,#4a4541 55%,#2a2826)}
.personal .mark{left:97px;top:96px;width:40px;height:40px;border:3px solid var(--white);border-radius:50%}
.personal h2{left:97px;top:140px;font-size:56px;font-weight:500;color:var(--white)}
.personal p{left:97px;top:218px;width:520px;color:var(--white);font-size:19px;line-height:1.8;text-align:justify}
.btn-gold{left:97px;top:385px;background:var(--gold);padding:20px 24px;font-size:16px;gap:22px}
.btn-gold .arr{background:var(--ink)}
.pcircle{width:226px;height:226px;border-radius:50%;border:6px solid var(--gold);background:radial-gradient(circle,#b07a22,#5e3a0e)}
/* testimonials */
.bubble{padding:44px 28px;font-size:15px;line-height:1.55;border-radius:22px}
.bubble.dark{background:var(--ink);color:var(--white)}
.bubble.gold{background:var(--gold);color:var(--white)}
.person{display:flex;align-items:center;gap:12px}
.avatar{width:78px;height:78px;border-radius:50%;background:linear-gradient(#cfcfcf,#8f8f8f);flex:none}
.person b{font-size:21px;font-weight:600;display:block}
.person small{font-size:12px;color:#555;display:block}
.stars{color:var(--gold);font-size:14px;letter-spacing:1px}
.arrow-btn{width:54px;height:54px;border-radius:50%;display:flex;align-items:center;justify-content:center}
/* footer */
.footer{top:4852px;left:0;width:1200px;height:373px;background:var(--ink);color:var(--white)}
.fcol{top:100px}
.fcol h5{font-size:21px;font-weight:500}
.fcol h5:after{content:"";display:block;width:38px;height:2px;background:var(--gold);margin-top:12px}
.fcol ul{list-style:none;margin-top:24px;font-size:14px}
.fcol li{line-height:26px;padding-left:24px;position:relative}
.fcol li:before{content:"»";position:absolute;left:0;color:var(--gold)}
.contact{display:flex;gap:20px;margin-bottom:14px;font-size:13px;line-height:1.35}
.contact .ic{width:30px;height:30px;background:var(--white);border-radius:4px;flex:none;display:flex;align-items:center;justify-content:center}
.bottom{top:5225px;left:0;width:1200px;height:43px;background:var(--ink);border-top:1px solid #333;color:var(--white);font-size:11px;padding:13px 68px;display:flex;gap:40px}
.cards{position:absolute;right:60px;top:14px;display:flex;gap:4px}
.cards span{width:26px;height:15px;background:#ddd;border-radius:2px}
</style>
</head>
<body>

<header class="abs header">
  <div class="abs brand"><span class="brand-dot"></span><span class="brand-name">TORVIK<br>LOOPS</span></div>
  <div class="abs search">Search...</div>
  <svg class="abs cart" width="30" height="28" viewBox="0 0 30 28"><path d="M2 4h5l4 14h13l3-10H9" fill="none" stroke="#111" stroke-width="3"/><circle cx="12" cy="23" r="2.5"/><circle cx="22" cy="23" r="2.5"/><circle cx="25" cy="5" r="5" fill="#d79a2b"/></svg>
  <nav class="abs nav"><a class="active">Home</a><a>Our Products ▾</a><a>Top Rated</a><a>Testimonials</a><a>About Us</a><a>Contact Us</a></nav>
</header>

<section class="abs hero" role="img" aria-label="Close-up photo of a man's hand wearing a rose gold ring with black inlay"></section>
<div class="abs hero-circle">
  <div class="eyebrow">TORVIK LOOPS</div>
  <h1 class="hero-title">Elevate Your<br>Style Handcrafted<br>Rings with Free Fast<br>Delivery &amp; Hassle<br>Free Returns</h1>
  <a class="btn">Shop Now <span class="arr"><svg width="12" height="12"><path d="M1 6h9M6 2l4 4-4 4" stroke="#111" stroke-width="2" fill="none"/></svg></span></a>
</div>

<section class="abs features">
  <div class="abs feature" style="left:92px"><div class="ring"><div class="core"><svg width="60" height="40"><rect x="2" y="6" width="38" height="24" fill="#fff"/><path d="M40 12h10l8 10v8H40z" fill="#fff"/><circle cx="14" cy="33" r="5" fill="#fff" stroke="#111" stroke-width="2"/><circle cx="48" cy="33" r="5" fill="#fff" stroke="#111" stroke-width="2"/></svg></div></div>Free Delivery</div>
  <div class="abs feature" style="left:342px"><div class="ring"><div class="core"><svg width="56" height="56"><path d="M10 28a18 18 0 1 0 6-13" fill="none" stroke="#fff" stroke-width="4"/><path d="M8 8l8 8-10 2z" fill="#fff"/><rect x="20" y="20" width="16" height="16" fill="#fff"/></svg></div></div>Free Returns</div>
  <div class="abs feature" style="left:604px"><div class="ring"><div class="core"><svg width="56" height="56"><ellipse cx="24" cy="32" rx="12" ry="16" fill="none" stroke="#fff" stroke-width="5"/><ellipse cx="34" cy="24" rx="12" ry="16" fill="none" stroke="#fff" stroke-width="5"/></svg></div></div>Every Ring Stock</div>
  <div class="abs feature" style="left:866px"><div class="ring"><div class="core"><svg width="60" height="40"><path d="M0 12h12M2 20h10M4 28h8" stroke="#fff" stroke-width="3"/><rect x="14" y="6" width="28" height="22" fill="#fff"/><path d="M42 12h8l8 9v7H42z" fill="#fff"/><circle cx="24" cy="32" r="5" fill="#fff" stroke="#111" stroke-width="2"/><circle cx="50" cy="32" r="5" fill="#fff" stroke="#111" stroke-width="2"/></svg></div></div>Fast Delivery</div>
</section>

<div class="abs sec-head" style="top:1176px"><div class="emblem"><i></i><b></b><i></i></div><h2 class="sec-title">Our Products</h2></div>

<div class="abs filter-title">Filter By:</div>
<div class="abs filter-label" style="left:66px">Select Color</div>
<div class="abs select" style="left:198px"></div>
<div class="abs filter-label" style="left:415px">Select Ring Size</div>
<div class="abs select" style="left:572px"></div>
<div class="abs filter-label" style="left:780px">Select Ring Width</div>
<div class="abs select" style="left:955px"></div>
<div class="abs filter-line"></div>

<div class="abs cat" style="left:68px;top:1505px"><div class="tile" role="img" aria-label="Photo of a black tungsten ring on a dark backdrop" style="background:radial-gradient(circle at 50% 55%,#5e5e5e,#111 75%)"><div class="the">THE</div><div class="name">BLACK</div><div class="coll">COLLECTION</div></div><div class="label">Black Rings for Men <i></i></div></div>
<div class="abs cat" style="left:432px;top:1505px"><div class="tile" role="img" aria-label="Photo of a brushed silver ring on a grey backdrop" style="background:radial-gradient(circle at 50% 55%,#a8a8a8,#2b2b2b 80%)"><div class="the">THE</div><div class="name">SILVER</div><div class="coll">COLLECTION</div></div><div class="label">Silver Rings for Men <i></i></div></div>
<div class="abs cat" style="left:795px;top:1505px"><div class="tile" role="img" aria-label="Photo of a black and blue titanium ring on a blue backdrop" style="background:radial-gradient(circle at 50% 55%,#1f4f8c,#06182e 80%)"><div class="the">THE</div><div class="name">BLUE</div><div class="coll">COLLECTION</div></div><div class="label">Blue Rings for Men <i></i></div></div>

<div class="abs cat" style="left:68px;top:2010px"><div class="tile" role="img" aria-label="Photo of a gold tungsten ring on a bronze backdrop" style="background:radial-gradient(circle at 50% 55%,#8f6d20,#1e1608 80%)"><div class="the">THE</div><div class="name">GOLD</div><div class="coll">COLLECTION</div></div><div class="label">Gold Rings for Men <i></i></div></div>
<div class="abs cat" style="left:432px;top:2010px"><div class="tile" role="img" aria-label="Photo of a silver ring with wood inlay on a brown backdrop" style="background:radial-gradient(circle at 50% 55%,#6e3a35,#2a1311 80%)"><div class="the">THE</div><div class="name">BROWN</div><div class="coll">COLLECTION</div></div><div class="label">Brown Rings for Men <i></i></div></div>
<div class="abs cat" style="left:795px;top:2010px"><div class="tile" role="img" aria-label="Photo of a rose gold and silver ring on a brown backdrop" style="background:radial-gradient(circle at 50% 55%,#6a4a42,#231512 80%)"><div class="the">THE</div><div class="name" style="font-size:54px">ROSE GOLD</div><div class="coll">COLLECTION</div></div><div class="label">Rose Gold Rings for Men <i></i></div></div>

<div class="abs sec-head" style="top:2562px"><div class="emblem"><i></i><b></b><i></i></div><h2 class="sec-title">Customer Favorites</h2></div>

<div class="abs card" style="left:70px;top:2713px"><div class="img" role="img" aria-label="Product photo of a black and blue titanium ring" style="background:linear-gradient(#f1f1f1,#e4e6ec)"></div><h3>Meridian - Black and Blue Titanium Rings</h3><div class="price"><s>£105.00</s>£45.00</div><a class="btn mini">Shop Now</a></div>
<div class="abs card" style="left:432px;top:2713px"><div class="img" role="img" aria-label="Product photo of a brushed silver and black tungsten ring" style="background:linear-gradient(#f1f1f1,#e4e4e4)"></div><h3>Vantage - Stylish Brushed Silver &amp; Black Tungsten Ring</h3><div class="price"><s>£115.00</s>£55.00</div><a class="btn mini">Shop Now</a></div>
<div class="abs card" style="left:794px;top:2713px"><div class="img" role="img" aria-label="Product photo of a traditional gold tungsten ring" style="background:linear-gradient(#f1f1f1,#ece6d8)"></div><h3>Regent - Traditional Men's Gold Ring in Tungsten</h3><div class="price"><s>£100.00</s>£65.00</div><a class="btn mini">Shop Now</a></div>

<a class="abs btn cta" style="top:3268px">View All Products <span class="arr"><svg width="12" height="12"><path d="M1 6h9M6 2l4 4-4 4" stroke="#111" stroke-width="2" fill="none"/></svg></span></a>

<section class="abs personal" role="img" aria-label="Background photo of hands exchanging a ring">
  <div class="abs mark"></div>
  <h2 class="abs">Personalization</h2>
  <p class="abs">Discover your perfect men's tungsten ring effortlessly. Each ring is a masterpiece, handcrafted with precision, offering unmatched strength, durability, and superior scratch resistance.</p>
  <a class="abs btn btn-gold">Personalize Your Ring <span class="arr"><svg width="12" height="12"><path d="M1 6h9M6 2l4 4-4 4" stroke="#fff" stroke-width="2" fill="none"/></svg></span></a>
  <div class="abs pcircle" role="img" aria-label="Photo of a black and silver ring" style="left:637px;top:62px"></div>
  <div class="abs pcircle" role="img" aria-label="Photo of a silver ring" style="left:872px;top:62px"></div>
  <div class="abs pcircle" role="img" aria-label="Photo of a gold ring" style="left:755px;top:262px"></div>
</section>

<div class="abs sec-head" style="top:4083px"><div class="emblem"><i></i><b></b><i></i></div><h2 class="sec-title">Our Testimonials</h2></div>

<div class="abs arrow-btn" style="left:67px;top:4393px;background:#aaa"><svg width="14" height="14"><path d="M10 1L4 7l6 6" stroke="#fff" stroke-width="2" fill="none"/></svg></div>
<div class="abs arrow-btn" style="left:1081px;top:4393px;background:var(--ink)"><svg width="14" height="14"><path d="M4 1l6 6-6 6" stroke="#fff" stroke-width="2" fill="none"/></svg></div>

<div class="abs bubble dark" style="left:213px;top:4245px;width:335px;height:220px">“ Lorem ipsum dolor sit amet, con sectetur adipiscing elit. Maece nas ac tellus ac ipsum porta viverra sit amet sed leo. Vivamus eu mauris convallis, hendrerit</div>
<svg class="abs" style="left:330px;top:4460px" width="80" height="60"><path d="M0 0h80L0 60z" fill="#111"/></svg>
<div class="abs person" style="left:240px;top:4525px"><span class="avatar" role="img" aria-label="Customer portrait"></span><div><b>Daniel Orwin</b><small>Lorem ipsum dolor</small><span class="stars">★★★★★</span></div></div>

<div class="abs person" style="left:675px;top:4255px"><span class="avatar" role="img" aria-label="Customer portrait"></span><div><b style="color:var(--gold)">Marcus Hale</b><small>Lorem ipsum dolor</small><span class="stars">★★★★★</span></div></div>
<svg class="abs" style="left:760px;top:4330px" width="90" height="62"><path d="M0 0l90 62H20z" fill="#d79a2b"/></svg>
<div class="abs bubble gold" style="left:655px;top:4390px;width:333px;height:215px">“ Lorem ipsum dolor sit amet, con sectetur adipiscing elit. Maece nas ac tellus ac ipsum porta viverra sit amet sed leo. Vivamus eu mauris convallis, hendrerit</div>

<a class="abs btn cta" style="top:4682px">View All Reviews <span class="arr"><svg width="12" height="12"><path d="M1 6h9M6 2l4 4-4 4" stroke="#111" stroke-width="2" fill="none"/></svg></span></a>

<footer class="abs footer">
  <div class="abs fcol" style="left:70px"><h5>Ring Guide</h5><ul><li>The Best Tungsten and Titanium Rings - Full Guide</li><li>How is Tungsten or Titanium Ring Size Measured?</li><li>Black, Silver Gold - The best colors for mens<br>tungsten and titanium rings</li><li>Whats better tungsten or titanium for a mens ring</li></ul></div>
  <div class="abs fcol" style="left:480px"><h5>Quick Links</h5><ul><li>FREE ring sizer</li><li>FREE Delivery</li><li>Returns and Exchanges</li><li>Try at Home</li><li>Ring Engraving</li></ul></div>
  <div class="abs fcol" style="left:703px"><h5>Important Links</h5><ul><li>Contact Us</li><li>Terms of Service</li><li>Privacy Policy</li><li>Blog</li></ul></div>
  <div class="abs fcol" style="left:908px"><h5>Contact Us</h5>
    <div style="margin-top:24px">
      <div class="contact"><span class="ic"><svg width="16" height="16"><path d="M3 1l4 4-2 2a9 9 0 0 0 4 4l2-2 4 4-2 2C7 15 1 9 1 3z" fill="#d79a2b"/></svg></span><div><b>CALL US</b><br>01632 960418</div></div>
      <div class="contact"><span class="ic"><svg width="16" height="12"><rect x="1" y="1" width="14" height="10" fill="none" stroke="#d79a2b" stroke-width="2"/><path d="M1 1l7 6 7-6" stroke="#d79a2b" stroke-width="2" fill="none"/></svg></span><div><b>EMAIL US</b><br>hello@torvikloops.com</div></div>
      <div class="contact"><span class="ic"><svg width="14" height="18"><path d="M7 17S1 10 1 6a6 6 0 0 1 12 0c0 4-6 11-6 11z" fill="#d79a2b"/><circle cx="7" cy="6" r="2" fill="#fff"/></svg></span><div>22 Quarry Lane, Elmbridge,<br>EB4 7QT</div></div>
    </div>
  </div>
</footer>
<div class="abs bottom"><span>© 2024 Torvik Loops</span><span>|</span><span>Veltrane Ltd - 09182736 - Incorporated on 20 April 2001</span><div class="cards"><span></span><span></span><span></span><span></span><span></span></div></div>

</body>
</html>
```